We need a business card design for a Dubai based company .

We need a business card for a Dubai based company called "Marwaneq Smoking Requisites Trading LLC". We mainly import Flavoured Tobacco products and Charcoal which is used for smoking in a Hookah/Shisha and distribute to the wholesalers and retailers. Logo file is attached herewith.

```html
<!DOCTYPE html>
<html lang="en">
<head>
<meta charset="utf-8">
<title>Marwaneq Business Card</title>
<link href="https://fonts.googleapis.com/css2?family=Montserrat:wght@400;500;700&display=swap" rel="stylesheet">
<style>
  :root {
    --page-bg: #3a332f;
    --card-black: #1c1c1c;
    --card-white: #ffffff;
    --brand-red: #b3161c;
    --ink: #1e1e1e;
    --ink-light: #f4f4f4;
  }
  html, body {
    margin: 0;
    padding: 0;
    width: 1200px;
    height: 716px;
    overflow: hidden;
    background: var(--page-bg);
    font-family: "Montserrat", sans-serif;
  }
  .canvas {
    position: relative;
    width: 1200px;
    height: 716px;
  }
  .card {
    position: absolute;
    top: 203px;
    width: 540px;
    height: 309px;
    box-sizing: border-box;
    box-shadow: 0 14px 30px rgba(0,0,0,0.45);
  }
  .card--front {
    left: 40px;
    background: var(--card-black);
    display: flex;
    align-items: center;
    justify-content: center;
  }
  .card--back {
    left: 620px;
    background: var(--card-white);
    display: flex;
    align-items: center;
    padding: 0 34px 0 40px;
  }
  .brand-name {
    font-weight: 500;
    text-align: center;
    line-height: 1;
  }
  .brand-name__word {
    display: block;
    font-size: 44px;
    letter-spacing: 6px;
  }
  .brand-name__line {
    display: block;
    margin-top: 10px;
    font-size: 9.5px;
    letter-spacing: 2.6px;
  }
  .card--front .brand-name { color: var(--ink-light); }
  .card--back .brand-name { color: var(--ink); width: 230px; }
  .card--back .brand-name__word { font-size: 30px; letter-spacing: 4px; }
  .card--back .brand-name__line { font-size: 6.6px; letter-spacing: 1.7px; margin-top: 8px; }
  .divider {
    width: 1.5px;
    height: 150px;
    background: var(--brand-red);
    margin: 0 22px 0 26px;
    flex-shrink: 0;
  }
  .contact {
    color: var(--ink);
    font-size: 12.5px;
    line-height: 1.35;
    letter-spacing: 0.4px;
  }
  .contact__name {
    color: var(--brand-red);
    font-weight: 700;
    font-size: 16px;
    letter-spacing: 1px;
    margin: 0;
  }
  .contact__title {
    margin: 0 0 2px;
    font-size: 12.5px;
    letter-spacing: 1px;
  }
  .contact__address { margin: 0; }
  .contact__list {
    list-style: none;
    margin: 0;
    padding: 0;
  }
  .contact__list li {
    display: flex;
    align-items: center;
    gap: 6px;
  }
  .contact__icon {
    width: 10px;
    height: 10px;
    flex-shrink: 0;
    stroke: var(--brand-red);
    fill: none;
    stroke-width: 1.6;
  }
</style>
</head>
<body>
<main class="canvas">
  <section class="card card--front" aria-label="Card front">
    <h1 class="brand-name">
      <span class="brand-name__word">MARWANEQ</span>
      <span class="brand-name__line">SMOKING REQUISITES TRADING LLC</span>
    </h1>
  </section>

  <section class="card card--back" aria-label="Card back">
    <div class="brand-name">
      <span class="brand-name__word">MARWANEQ</span>
      <span class="brand-name__line">SMOKING REQUISITES TRADING LLC</span>
    </div>
    <div class="divider"></div>
    <div class="contact">
      <p class="contact__name">DANIEL HART</p>
      <p class="contact__title">DIRECTOR</p>
      <p class="contact__address">4470 Harbor Lane,<br>Suite 318 Springfield, OH</p>
      <ul class="contact__list">
        <li>
          <svg class="contact__icon" viewBox="0 0 12 12"><path d="M3 1 L5 3.5 L4 5 Q5 7.5 7 8 L8.5 7 L11 9 L9.5 11 Q3 10 1 2.5 Z"/></svg>
          5550142387
        </li>
        <li>
          <svg class="contact__icon" viewBox="0 0 12 12"><rect x="1" y="2.5" width="10" height="7"/><path d="M1 2.5 L6 6.5 L11 2.5"/></svg>
          info@marwaneq.com
        </li>
        <li>
          <svg class="contact__icon" viewBox="0 0 12 12"><circle cx="6" cy="6" r="5"/><ellipse cx="6" cy="6" rx="2.2" ry="5"/><path d="M1 6 H11"/></svg>
          www.marwaneq.com
        </li>
      </ul>
    </div>
  </section>
</main>
</body>
</html>
```